Sleek business card design for digital agency.

Brief document attached for detailed description and inspiration. Looking for a minimalist sleek, cool, modern business card design.

Industry/Entity Type

Digital

```html
<!DOCTYPE html>
<html lang="en">
<head>
<meta charset="utf-8">
<title>Fennec Works — Business Card</title>
<link rel="stylesheet" href="https://fonts.googleapis.com/css2?family=Questrial&display=swap">
<style>
  :root {
    --backdrop: #3a2419;
    --card: #201d22;
    --card-deep: #0b0a0c;
    --art-dark: #050505;
    --logo-dim: #0c0b0d;
    --logo-tab: #232025;
    --ink: #ffffff;
    --accent: #2ba4dc;
  }
  * { margin: 0; padding: 0; box-sizing: border-box; }
  html, body {
    width: 1200px; height: 1181px; overflow: hidden;
    background: var(--backdrop);
    font-family: "Questrial", "Century Gothic", sans-serif;
  }
  .canvas { position: relative; width: 1200px; height: 1181px; }

  .card {
    position: absolute; left: 207px; width: 786px; height: 453px;
    border-radius: 32px; overflow: hidden;
    background: var(--card);
  }
  .card--front { top: 103px; }
  .card--back { top: 615px; }

  .front-art {
    position: absolute; inset: 0; z-index: 0;
    background:
      radial-gradient(ellipse 330px 300px at 67% 55%, var(--art-dark) 0%, var(--art-dark) 55%, transparent 72%),
      radial-gradient(ellipse 300px 150px at 15% 98%, var(--art-dark) 0%, var(--art-dark) 55%, transparent 75%),
      linear-gradient(135deg, #1e1b20 0%, #141215 100%);
  }
  .front-logo {
    position: absolute; left: 30px; top: 182px; z-index: 1;
    font-size: 34px; line-height: 40px; color: var(--logo-dim); letter-spacing: -0.3px;
    white-space: nowrap;
  }

  .logo-tab {
    position: absolute; left: 258px; top: 0; width: 268px; height: 143px;
    background: var(--card-deep);
    border-radius: 0 0 30px 30px;
    display: flex; align-items: center; justify-content: center;
  }
  .logo-tab__name { font-size: 32px; color: var(--logo-tab); letter-spacing: -0.3px; white-space: nowrap; }

  .identity {
    position: absolute; left: 0; right: 0; top: 194px;
    text-align: center; color: var(--ink);
  }
  .identity__name { font-size: 27px; font-weight: 700; letter-spacing: 1.5px; line-height: 30px; }
  .identity__role { font-size: 16px; color: var(--accent); letter-spacing: 3px; line-height: 19px; }
  .identity__note { font-size: 13.5px; line-height: 16px; }

  .address {
    position: absolute; left: 0; right: 0; top: 365px;
    text-align: center; color: var(--ink); font-style: normal;
    font-size: 10.5px; font-weight: 700; line-height: 15px; letter-spacing: 0.4px;
  }
  .contacts {
    position: absolute; left: 0; right: 0; top: 403px;
    display: flex; justify-content: center;
    color: var(--ink); font-size: 10.5px; font-weight: 700; line-height: 16px; letter-spacing: 0.4px;
  }
  .contacts__col { padding: 0 9px; white-space: nowrap; }
  .contacts__col--web { text-align: right; }
  .contacts__col + .contacts__col { border-left: 1.5px solid var(--accent); }
</style>
</head>
<body>
<main class="canvas">
  <section class="card card--front">
    <div class="front-art" role="img" aria-label="Large dark silhouette illustration spreading across the card face"></div>
    <div class="front-logo">Fennec Works</div>
  </section>

  <section class="card card--back">
    <div class="logo-tab"><span class="logo-tab__name">Fennec Works</span></div>

    <div class="identity">
      <p class="identity__name">Daniel Ashby</p>
      <p class="identity__role">Marketing Director</p>
      <p class="identity__note">Drink order: G&amp;T with cucumber</p>
    </div>

    <address class="address">
      Level 3, 18 Harlow St<br>East Marden NSW 5000
    </address>

    <div class="contacts">
      <div class="contacts__col contacts__col--web">dashby@fennecworks.com<br>www.fennecworks.com</div>
      <div class="contacts__col">0400 555 812<br>03 9000 4127</div>
      <div class="contacts__col">@dashby81<br>social.fennecworks.com</div>
    </div>
  </section>
</main>
</body>
</html>
```